Brightwell Power Solutions

We'd like a web design that's beautiful and professional. We replace existing inefficient systems (mostly lighting at the moment but expanding) with highly efficient systems.

```html
<!DOCTYPE html>
<html lang="en">
<head>
<meta charset="utf-8">
<title>Brightwell Power Solutions</title>
<link rel="stylesheet" href="https://fonts.googleapis.com/css2?family=Ubuntu:wght@300;400;500&family=Questrial&family=Arimo:wght@400&display=swap">
<style>
:root{
  --green:#0f9a3e;
  --green-dark:#0b7f31;
  --ink:#1f1f1f;
  --dark:#1c1c1c;
  --grey-text:#6b6b6b;
  --light:#f2f2f2;
  --white:#ffffff;
}
*{margin:0;padding:0;box-sizing:border-box}
html,body{width:733px;height:1200px;overflow:hidden}
body{position:relative;background:#e8e8e8;font-family:"Ubuntu",sans-serif;color:var(--ink)}
.abs{position:absolute}

.site-header{left:0;top:0;width:733px;height:88px;background:#f4f4f4}
.brand{left:68px;top:16px;display:flex;align-items:center;gap:8px}
.brand-square{width:18px;height:18px;background:var(--green)}
.brand-name{font-family:"Ubuntu",sans-serif;font-weight:500;font-size:13px;line-height:15px;color:var(--green);letter-spacing:1px}
.header-contact{right:36px;top:20px;text-align:right;font-size:9.5px;color:#666;line-height:17px}
.header-contact svg{vertical-align:-2px;margin-right:5px}
.social{right:35px;top:58px;display:flex;gap:5px}
.social span{width:19px;height:19px;border-radius:50%;display:block}

.main-nav{left:0;top:88px;width:733px;height:38px;background:linear-gradient(#17a84a,#0d8f38)}
.main-nav ul{list-style:none;display:flex;position:absolute;left:48px;top:0;height:38px;align-items:center}
.main-nav li{font-family:"Arimo",sans-serif;font-size:10px;color:var(--white);padding:0 18px;border-right:1px solid rgba(0,0,0,.2);line-height:22px}
.main-nav li:last-child{border-right:none}
.search{left:563px;top:95px;width:135px;height:24px;display:flex}
.search-field{flex:1;background:var(--white);font-size:9.5px;color:#aaa;padding:5px 10px}
.search-btn{width:41px;background:#222;display:flex;align-items:center;justify-content:center}

.hero{left:0;top:126px;width:733px;height:214px;background:radial-gradient(ellipse at 50% 25%,#fafafa 0%,#d9d9d9 55%,#bdbdbd 100%)}
.hero-visual{left:175px;top:132px;width:360px;height:208px;background:radial-gradient(ellipse at 50% 30%,rgba(255,255,255,.9),rgba(200,200,200,.2) 70%)}
.hero-title{left:0;top:176px;width:733px;text-align:center;font-family:"Questrial",sans-serif;font-size:29px;color:var(--green);letter-spacing:.3px}
.hero-arrow{top:232px;font-size:30px;color:#888;font-family:"Questrial",sans-serif}

.cta-bar{left:28px;top:340px;width:676px;height:46px}
.cta-label{font-family:"Questrial",sans-serif;font-variant:small-caps;font-size:15px;color:var(--white);letter-spacing:.6px}

.welcome-band{left:0;top:386px;width:733px;height:274px;background:linear-gradient(#c6c6c6,#e0e0e0)}
.welcome{left:68px;top:410px;width:280px}
.welcome h1{font-weight:400;font-size:14px;white-space:nowrap;color:var(--ink);padding-bottom:10px;border-bottom:1px solid #b5b5b5}
.welcome h1 em{font-style:normal;color:var(--green)}
.welcome p{font-size:8.7px;line-height:17.6px;color:#666;margin-top:10px;padding-bottom:14px;border-bottom:1px solid #bdbdbd}

.audit-panel{left:397px;top:395px;width:243px;height:270px;background:linear-gradient(#8d8d8d,#6f6f6f)}
.audit-head{left:389px;top:406px;width:257px;height:29px;background:#232323;color:var(--white);font-size:14px;padding:4px 0 0 26px}
.audit-head em{font-style:normal;color:var(--green)}
.audit-head svg{vertical-align:-2px;margin-right:6px}
.field{left:412px;width:217px;background:var(--white);border:1px solid #ddd;font-size:10.5px;color:#999;padding:6px 10px}
.field.message{border-color:var(--green)}
.send{left:412px;top:610px;width:217px;height:27px;background:linear-gradient(#3a3a3a,#111);color:#eee;font-size:11px;text-align:center;line-height:27px}

.unique{left:68px;top:690px;width:597px;height:264px;background:#dedede}
.unique-head{height:28px;background:var(--green);color:var(--white);font-size:14px;padding:5px 0 0 27px}
.unique ul{list-style:none;position:absolute;top:52px}
.unique li{position:relative;padding-left:20px;font-size:9.3px;line-height:14px;color:#666;margin-bottom:14px}
.unique li svg{position:absolute;left:3px;top:3px}
.col-left{left:18px;width:272px}
.col-right{left:316px;width:266px}

.site-footer{left:0;top:1000px;width:733px;height:172px;background:#1b1b1b}
.foot-col{top:1020px}
.foot-col h2{font-family:"Arimo",sans-serif;font-weight:400;font-size:11.5px;color:#eee;padding-bottom:11px;border-bottom:1px solid #444;width:156px}
.foot-col ul{list-style:none;margin-top:9px}
.foot-col li{font-family:"Arimo",sans-serif;font-size:8.8px;color:#eee;line-height:21.5px;padding-left:14px;position:relative}
.foot-col .dots li::before{content:"";position:absolute;left:4px;top:9px;width:4px;height:4px;border-radius:50%;background:#eee}
.foot-col .icons li{padding-left:17px}
.foot-col .icons svg{position:absolute;left:2px;top:7px}
.link-grid{display:grid;grid-template-columns:86px 80px}

.bottom-bar{left:0;top:1172px;width:733px;height:28px;background:var(--green)}
.bottom-social{left:77px;top:1179px;display:flex;gap:5px}
.bottom-social span{width:15px;height:15px;border-radius:50%;background:var(--white);display:block}
.copyright{right:71px;top:1181px;font-family:"Arimo",sans-serif;font-size:7.5px;color:var(--white)}
</style>
</head>
<body>

<header class="abs site-header"></header>
<div class="abs brand">
  <span class="brand-square"></span>
  <div class="brand-name">BRIGHTWELL<br>POWER SOLUTIONS</div>
</div>
<div class="abs header-contact">
  <div><svg width="11" height="8" viewBox="0 0 11 8"><path d="M0 3 Q5.5 -1 11 3 L9 4 L8 2.5 L3 2.5 L2 4 Z M2 4.5 H9 V8 H2 Z" fill="#0f9a3e"/></svg>1-855-555-0142</div>
  <div><svg width="11" height="8" viewBox="0 0 11 8"><rect width="11" height="8" fill="#0f9a3e"/><path d="M0 0 L5.5 4.5 L11 0" stroke="#fff" fill="none"/></svg>hello@brightwellpower.com</div>
</div>
<div class="abs social">
  <span style="background:#3b7fb0"></span>
  <span style="background:#3fa0e0"></span>
  <span style="background:#2f4f97"></span>
  <span style="background:#d42d22"></span>
</div>

<nav class="abs main-nav">
  <ul>
    <li>HOME</li><li>WHY LED?</li><li>CASE STUDIES</li><li>FAQ</li><li>ENERGY AUDIT</li><li>CONTACT</li>
  </ul>
</nav>
<div class="abs search">
  <div class="search-field">Search...</div>
  <div class="search-btn"><svg width="14" height="14" viewBox="0 0 14 14"><circle cx="5" cy="5" r="3.8" stroke="#fff" stroke-width="1.8" fill="none"/><path d="M8 8 L13 13" stroke="#fff" stroke-width="2.4"/></svg></div>
</div>

<section class="abs hero"></section>
<div class="abs hero-visual" role="img" aria-label="Glowing LED bulb above a circle of clear light bulbs"></div>
<div class="abs hero-title">PROMOTING ENERGY INDEPENDENCE</div>
<div class="abs hero-arrow" style="left:33px">&#10094;</div>
<div class="abs hero-arrow" style="left:678px">&#10095;</div>

<svg class="abs cta-bar" width="676" height="46" viewBox="0 0 676 46">
  <polygon points="0,0 330,0 345,23 330,46 0,46" fill="#1f1f1f"/>
  <polygon points="330,0 340,0 355,23 340,46 330,46 345,23" fill="#fff"/>
  <polygon points="340,0 676,0 676,46 340,46 355,23" fill="#0f9a3e"/>
</svg>
<div class="abs cta-label" style="left:98px;top:353px">LED Lighting Solutions <b>?</b></div>
<div class="abs cta-label" style="left:393px;top:353px">
  <svg width="17" height="12" viewBox="0 0 11 8" style="vertical-align:-1px;margin-right:6px"><path d="M0 3 Q5.5 -1 11 3 L9 4 L8 2.5 L3 2.5 L2 4 Z M2 4.5 H9 V8 H2 Z" fill="#fff"/></svg>1-855-GLOW-LED (1-855-555-0142)
</div>

<section class="abs welcome-band"></section>
<div class="abs welcome">
  <h1>Welcome to <em>Brightwell Power Solutions</em></h1>
  <p>Brightwell Power Solutions is an acknowledged Green Energy leader providing energy saving lighting solutions. Our GBEP trained professionals coupled with our close relationships with the leading LED manufacturers around the world, ensures that your LED retrofit project will be affordable; saving you up to 75% on your lighting costs and drastically reducing replacement costs. Our turn-key system takes care of everything from the initial lighting energy audit, to an energy saving solution, to professional installation, and finally complete cleanup and proper disposal.</p>
</div>

<div class="abs audit-panel"></div>
<div class="abs audit-head"><svg width="13" height="13" viewBox="0 0 13 13"><rect x="1" y="2" width="10" height="10" stroke="#fff" fill="none" stroke-width="1.3"/><path d="M3 6 L6 9 L12 1" stroke="#fff" fill="none" stroke-width="1.8"/></svg>Request a <em>free Audit</em></div>
<div class="abs field" style="top:446px;height:27px">Name</div>
<div class="abs field" style="top:479px;height:27px">Contact No.</div>
<div class="abs field message" style="top:513px;height:85px">Message</div>
<div class="abs send">Send Message</div>

<section class="abs unique">
  <div class="unique-head">Why we are unique?</div>
  <ul class="col-left">
    <li><svg width="11" height="9" viewBox="0 0 11 9"><path d="M1 5 L4 8 L10 1" stroke="#0f9a3e" stroke-width="2" fill="none"/></svg>Established in 1986 with 25 years of outstanding service, a GSA approved vendor</li>
    <li><svg width="11" height="9" viewBox="0 0 11 9"><path d="M1 5 L4 8 L10 1" stroke="#0f9a3e" stroke-width="2" fill="none"/></svg>A Service-Disabled Veteran-Owned company focused on hiring Service Disabled Veterans, Veterans and family members of veterans</li>
    <li><svg width="11" height="9" viewBox="0 0 11 9"><path d="M1 5 L4 8 L10 1" stroke="#0f9a3e" stroke-width="2" fill="none"/></svg>As a member of the Greenfield Building Alliance, we support green design, construction and operations</li>
    <li><svg width="11" height="9" viewBox="0 0 11 9"><path d="M1 5 L4 8 L10 1" stroke="#0f9a3e" stroke-width="2" fill="none"/></svg>GBEP (Green Building Efficiency Program) trained employees</li>
  </ul>
  <ul class="col-right">
    <li><svg width="11" height="9" viewBox="0 0 11 9"><path d="M1 5 L4 8 L10 1" stroke="#0f9a3e" stroke-width="2" fill="none"/></svg>DUNS Number - 000000000</li>
    <li><svg width="11" height="9" viewBox="0 0 11 9"><path d="M1 5 L4 8 L10 1" stroke="#0f9a3e" stroke-width="2" fill="none"/></svg>Active in Federal Vendor Registry (FVR) - Registration valid until 07/15/2014</li>
    <li><svg width="11" height="9" viewBox="0 0 11 9"><path d="M1 5 L4 8 L10 1" stroke="#0f9a3e" stroke-width="2" fill="none"/></svg>Registered NAICS codes - 000100, 000200, 000300</li>
    <li><svg width="11" height="9" viewBox="0 0 11 9"><path d="M1 5 L4 8 L10 1" stroke="#0f9a3e" stroke-width="2" fill="none"/></svg>LED products available on GSA Schedule - GS-00X-0000A</li>
    <li><svg width="11" height="9" viewBox="0 0 11 9"><path d="M1 5 L4 8 L10 1" stroke="#0f9a3e" stroke-width="2" fill="none"/></svg>CAGE Code - 0X0X0</li>
  </ul>
</section>

<footer class="abs site-footer"></footer>
<div class="abs foot-col" style="left:75px">
  <h2>QUICKLINKS</h2>
  <ul class="dots link-grid">
    <li>Home</li><li>FAQ</li><li>Why LED?</li><li>Energy Audit</li><li>Case Studies</li><li>Contact</li>
  </ul>
</div>
<div class="abs foot-col" style="left:273px">
  <h2>CONTACT INFORMATION</h2>
  <ul class="icons">
    <li><svg width="9" height="8" viewBox="0 0 9 8"><path d="M0 4 L4.5 0 L9 4 H7.5 V8 H1.5 V4 Z" fill="#fff"/></svg>Loc: 123 Address, City. Country</li>
    <li><svg width="9" height="7" viewBox="0 0 11 8"><path d="M0 3 Q5.5 -1 11 3 L9 4 L8 2.5 L3 2.5 L2 4 Z M2 4.5 H9 V8 H2 Z" fill="#fff"/></svg>Tel: 02-5550-193847</li>
    <li><svg width="10" height="7" viewBox="0 0 11 8"><rect width="11" height="8" fill="#fff"/><path d="M0 0 L5.5 4.5 L11 0" stroke="#1b1b1b" fill="none"/></svg>Email: hello@brightwellpower.com</li>
    <li><svg width="10" height="7" viewBox="0 0 11 8"><rect width="11" height="8" fill="#fff"/><path d="M0 0 L5.5 4.5 L11 0" stroke="#1b1b1b" fill="none"/></svg>Chat: hello@brightwellpower.com</li>
  </ul>
</div>
<div class="abs foot-col" style="left:491px">
  <h2>THE BOTTOMLINE</h2>
  <ul class="dots">
    <li>The Savings</li><li>LED Retrofit Process</li><li>Tax Incentives</li><li>Utility Rebates</li>
  </ul>
</div>

<div class="abs bottom-bar"></div>
<div class="abs bottom-social"><span></span><span></span><span></span><span></span></div>
<div class="abs copyright">Copyright © 2014. Brightwell Power Solutions All Rights Reserved.</div>

</body>
</html>
```